Standard Biz Card
Health Professionals
Please upload ai or eps of your logo
Kindly upload logo file in ai/eps format!
That contest is here: http://orders.markcraftplaza.example/contests/new-health-clinic-logo-biz-card
Sorry, there seem to be a misunderstandig as we thought this job was combined with the logo job. We do not have a logo yet, it is another contest going on at the moment.
Please upload the logo files

```html
<!DOCTYPE html>
<html lang="no">
<head>
<meta charset="utf-8">
<title>Visittkort – Lars Eriksen</title>
<link rel="stylesheet" href="https://fonts.googleapis.com/css2?family=Source+Sans+3:wght@400;600&display=swap">
<style>
  :root {
    --page: #ffffff;
    --card-edge: #b9bcc0;
    --panel-light-1: #f7f7f8;
    --panel-light-2: #e4e5e7;
    --logo-blue: #1872bf;
    --divider-blue: #1567b8;
    --panel-blue-top: #2570bf;
    --panel-blue-mid: #5f9fd6;
    --panel-blue-bottom: #a6dbea;
    --ink-white: #ffffff;
  }
  * { box-sizing: border-box; margin: 0; padding: 0; }
  html, body {
    width: 1200px; height: 814px; overflow: hidden;
    background: var(--page);
    font-family: "Source Sans 3", "Myriad Pro", Arial, sans-serif;
  }
  .canvas { position: relative; width: 1200px; height: 814px; }
  .business-card {
    position: absolute; left: 53px; top: 96px; width: 1092px; height: 622px;
    border: 2px solid var(--card-edge);
    display: flex; overflow: hidden;
  }
  .brand-panel {
    position: relative; width: 576px; height: 100%;
    background: linear-gradient(90deg, var(--panel-light-1), var(--panel-light-2));
  }
  .logo-placeholder {
    position: absolute; left: 118px; top: 142px; width: 340px; height: 338px;
    background: var(--logo-blue);
    display: flex; align-items: center; justify-content: center;
    color: var(--ink-white); font-size: 42px; font-weight: 400; letter-spacing: 0.5px;
  }
  .panel-divider { width: 8px; height: 100%; background: var(--divider-blue); }
  .contact-panel {
    position: relative; flex: 1; height: 100%;
    background: linear-gradient(180deg, var(--panel-blue-top) 0%, var(--panel-blue-mid) 50%, var(--panel-blue-bottom) 100%);
    color: var(--ink-white);
  }
  .person-name {
    position: absolute; left: 25px; top: 88px;
    font-size: 41px; font-weight: 600; line-height: 1;
  }
  .person-title {
    position: absolute; left: 26px; top: 151px;
    font-size: 25px; font-weight: 400; line-height: 1;
  }
  .contact-list {
    position: absolute; left: 26px; top: 384px;
    list-style: none; font-size: 25px; line-height: 36px; font-weight: 400;
  }
</style>
</head>
<body>
  <main class="canvas">
    <section class="business-card">
      <div class="brand-panel">
        <div class="logo-placeholder">YOUR LOGO</div>
      </div>
      <div class="panel-divider"></div>
      <div class="contact-panel">
        <h1 class="person-name">Lars Eriksen</h1>
        <p class="person-title">Manuellterapeut</p>
        <ul class="contact-list">
          <li>Solbakkveien 4, 1366 Lysaker</li>
          <li>P: 00 00 00 00</li>
          <li>F: 00 00 00 00</li>
          <li>E: post@balansemt.no</li>
          <li>www.balansemt.no</li>
        </ul>
      </div>
    </section>
  </main>
</body>
</html>
```